Popup Banners - BrightCounsel - Legal Technology

- We need two banners (same style) designed with two different images and different text.

- The details of the printing requirements are attached, along with suggested images.

- The banners should share the same theme as our website www.brightcounsel.com.au

- The first banner would include our logo (attached), use the 'roads join' image (attached) in some way and text: New Opportunities - Where legal services and technology meet.

- The second banner would include our logo (attached), use the 'jigsaw' image (attached) in some way and use text: Legal Technology Strategy, Advice and Capability.

- Details on what are required from the Printer is attached also.

Target Market(s)

Legal Professionals

Industry/Entity Type

Information Technology

Font styles to use
Sans Serif

Requirements
Must have
• Our logo (attached), suggested text and the image mentioned for each.
Nice to have
• Professional and modern look
Should not have
• Cheap looking

```html
<!DOCTYPE html>
<html lang="en">
<head>
<meta charset="utf-8">
<title>BrightCounsel – Legal Technology Banners</title>
<link rel="stylesheet" href="https://fonts.googleapis.com/css2?family=Open+Sans:wght@400;600;700&display=swap">
<style>
  :root {
    --page-bg: #f7f8f8;
    --band-blue: #4a82b8;
    --navy: #243a56;
    --white: #ffffff;
    --dot-blue: #5b93cc;
    --glow-core: #f2f8ff;
    --glow-soft: #a9cdf5;
    --jigsaw-mid: #3f74b4;
    --jigsaw-deep: #284a7a;
    --sky-low: #4a6888;
    --grass-top: #5f8a34;
    --grass-mid: #4c7a28;
    --grass-deep: #3b6420;
    --grass-light: #79a445;
  }
  * { box-sizing: border-box; margin: 0; padding: 0; }
  html, body {
    width: 1200px; height: 858px; overflow: hidden;
    background: var(--page-bg);
    font-family: "Open Sans", Arial, sans-serif;
  }
  .banner-row {
    width: 1200px; height: 858px;
    display: flex; justify-content: center; align-items: center; gap: 60px;
  }
  .banner {
    position: relative;
    width: 323px; height: 760px;
    background: var(--navy);
    overflow: hidden;
    box-shadow: 0 2px 8px rgba(0,0,0,0.12);
  }
  .brand-band {
    position: relative; z-index: 2;
    height: 100px;
    background: var(--band-blue);
    display: flex; align-items: center; justify-content: center; gap: 12px;
  }
  .brand-mark { width: 16px; height: 16px; background: var(--white); }
  .brand-name {
    color: var(--white); font-weight: 600; font-size: 21px; letter-spacing: 0.18em;
  }
  .copy {
    position: relative; z-index: 2;
    text-align: center; color: var(--white);
  }
  .headline { font-weight: 400; text-transform: uppercase; }
  .banner--jigsaw .copy { padding-top: 46px; }
  .banner--jigsaw .headline { font-size: 22px; letter-spacing: 0.04em; }
  .service-list {
    list-style: none; margin-top: 14px;
    font-weight: 700; font-size: 10px; letter-spacing: 0.06em;
  }
  .service-list li { line-height: 14px; }
  .service-list .dot {
    display: block; width: 4px; height: 4px; border-radius: 50%;
    background: var(--dot-blue); margin: 6px auto;
  }
  .jigsaw-photo {
    position: absolute; left: 0; right: 0; bottom: 0; height: 440px;
    background:
      radial-gradient(ellipse 150px 140px at 44% 46%, var(--glow-core) 0%, var(--glow-soft) 30%, rgba(90,145,215,0.55) 65%, rgba(63,116,180,0) 100%),
      linear-gradient(180deg, var(--navy) 0%, var(--jigsaw-deep) 22%, var(--jigsaw-mid) 60%, var(--jigsaw-deep) 100%);
  }
  .banner--roads .copy { padding-top: 38px; }
  .banner--roads .headline { font-size: 20px; line-height: 37px; letter-spacing: 0.08em; }
  .roads-photo {
    position: absolute; left: 0; right: 0; bottom: 0; height: 560px;
    background: linear-gradient(180deg,
      var(--navy) 0%, var(--navy) 18%, var(--sky-low) 40%, var(--sky-low) 46%,
      var(--grass-top) 46.5%, var(--grass-mid) 62%, var(--grass-deep) 78%, var(--grass-light) 100%);
  }
</style>
</head>
<body>
  <main class="banner-row">
    <section class="banner banner--jigsaw">
      <header class="brand-band">
        <span class="brand-mark"></span><span class="brand-name">BrightCounsel</span>
      </header>
      <div class="jigsaw-photo" role="img" aria-label="Hand holding a glowing jigsaw piece against a blue puzzle background"></div>
      <div class="copy">
        <h1 class="headline">Legal Technology</h1>
        <ul class="service-list">
          <li>STRATEGY</li><li class="dot"></li>
          <li>ADVICE</li><li class="dot"></li>
          <li>AND</li><li class="dot"></li>
          <li>CAPABILITY</li>
        </ul>
      </div>
    </section>

    <section class="banner banner--roads">
      <header class="brand-band">
        <span class="brand-mark"></span><span class="brand-name">BrightCounsel</span>
      </header>
      <div class="roads-photo" role="img" aria-label="Two dirt roads joining on a green grassy hill under a dusky sky"></div>
      <div class="copy">
        <h1 class="headline">New Opportunities<br>Where Legal<br>Services and<br>Technology<br>Meet</h1>
      </div>
    </section>

    <section class="banner banner--jigsaw">
      <header class="brand-band">
        <span class="brand-mark"></span><span class="brand-name">BrightCounsel</span>
      </header>
      <div class="jigsaw-photo" role="img" aria-label="Hand holding a glowing jigsaw piece against a blue puzzle background"></div>
      <div class="copy">
        <h1 class="headline">Legal Technology</h1>
        <ul class="service-list">
          <li>STRATEGY</li><li class="dot"></li>
          <li>ADVICE</li><li class="dot"></li>
          <li>AND</li><li class="dot"></li>
          <li>CAPABILITY</li>
        </ul>
      </div>
    </section>
  </main>
</body>
</html>
```